Buttons, Banners & MPUs - 'Alpine Getaway Journal'

We are launching a new product - a bookazine on sale later this month!

General description below:

ALPINE GETAWAY JOURNALS 2015

Calling all lovers of French holidays! Where will you go in 2015?

Let us guide you to the very best holidays in France with our brand new guide, featuring 180 pages of high quality and inspiring editorial and imagery. Alpine Getaway Journals 2015 provides a comprehensive, ideas-packed guide to classic breaks, as well as niche and new holiday ideas across France.

Love to get out in the French fresh air? We have activities such as boating, cycling and golf covered. There’s plenty for culture vultures and city breakers, too, plus lots of great ideas for family breaks including theme parks, zoos and attractions.

We whet the appetite of foodies and wine lovers, provide a guide to markets and festivals and also get off the beaten track with guides to driving, railway holidays and visit some of France’s most beautiful villages. And if you want to get creative, there are loads of ideas for photography, art, ‘me time’ escapes and tempting snapshots of some of France’s most unusual accommodation.

Whatever you love about France, there’s a fabulous Alpine Getaway made for you!

Design brief - bright, fun, exciting, inspiring.. with a clear call-to-action

We require a variety of sizes including:
300 x 250, 250 x 250, 728 x 90, 468 x 60, 120 x 600, 120 x 240, 600 x 200
- please only create a couple to showcase your design

More information can be found on the products website but please be aware that this is still under construction so please do not base your design on this: http://www.alpinegetawayjournals.com/

Target Market(s)

Francophiles, holiday makers, 40+, families, couples,

Font styles to use
Serif
Sans Serif

Requirements
Must have
• Logo
• Call to action
Nice to have
• Suggested strap lines:
• - The ultimate guide to holidays in France
• - The biggest and best guide to France
• - 180 pages of Fabulous Alpine Getaway Ideas
• - What's New in 2015
Should not have
• Price - we want to direct traffic to our website which will reflect their local currency

```html
<!DOCTYPE html>
<html lang="en">
<head>
<meta charset="utf-8">
<title>Alpine Getaway Journals 2015 – Banner Set</title>
<link rel="stylesheet" href="https://fonts.googleapis.com/css2?family=Source+Sans+3:wght@400;600;700&display=swap">
<style>
  :root {
    --stage: #202020;
    --navy: #24237a;
    --navy-deep: #1b1a66;
    --red: #e32b36;
    --paper: #eef2f7;
    --white: #ffffff;
    --text-font: "Source Sans 3", Arial, sans-serif;
  }
  * { box-sizing: border-box; margin: 0; padding: 0; }
  html, body { width: 1200px; height: 915px; overflow: hidden; }
  body { background: var(--stage); font-family: var(--text-font); position: relative; }

  .banner { position: absolute; overflow: hidden; background: var(--paper); }
  .photo { position: absolute; }
  .flag-band { position: absolute; left: 0; right: 0; top: 0; height: 8px;
    background: linear-gradient(90deg, var(--navy) 0 33%, var(--white) 33% 66%, var(--red) 66%); }
  .fade { position: absolute; left: 0; right: 0; top: 0; background: rgba(255,255,255,.82); }

  .brand { position: absolute; font-weight: 700; color: var(--navy); line-height: .95; letter-spacing: -1px; white-space: nowrap; }
  .brand small { display: block; font-size: .32em; letter-spacing: 0; text-align: right; line-height: 1.1; }
  .brand.on-dark { color: var(--white); }

  .tag { position: absolute; color: var(--white); font-weight: 600; white-space: nowrap; padding: 0 9px; display: flex; align-items: center; }
  .tag.red { background: var(--red); }
  .tag.navy { background: var(--navy); font-weight: 700; }

  .line-tag { position: absolute; background: var(--white); color: var(--navy); white-space: nowrap; font-size: 15px; padding: 1px 6px; }
  .line-tag.strong { font-weight: 700; }
  .line-tag.bar-left { border-left: 4px solid var(--navy); }
  .line-tag.bar-right { border-right: 4px solid var(--navy); font-size: 13px; }

  .cta { position: absolute; display: flex; align-items: center; justify-content: center; color: var(--white);
    font-weight: 600; font-size: 14px; border-radius: 2px; text-decoration: none;
    background: linear-gradient(180deg, #302f92, var(--navy-deep)); box-shadow: 0 1px 3px rgba(0,0,0,.4); }

  .bubble { position: absolute; border-radius: 50%; display: flex; align-items: center; justify-content: center;
    text-align: center; color: var(--white); font-weight: 700; line-height: 1; }
  .bubble.red { background: var(--red); z-index: 2; }
  .bubble.navy { background: var(--navy); }

  .base-band { position: absolute; left: 0; right: 0; bottom: 0; height: 8px; background: var(--navy-deep); }
</style>
</head>
<body>

  <!-- 120 x 600 skyscraper -->
  <section class="banner skyscraper" style="left:144px;top:164px;width:121px;height:606px;">
    <div class="photo" role="img" aria-label="Photo of a French town square with historic facades" style="left:0;top:280px;width:121px;height:326px;background:linear-gradient(180deg,#dfe3ea 0%,#c9a596 30%,#b89a82 60%,#cfc3b8 100%);"></div>
    <div class="flag-band"></div>
    <div class="brand" style="left:5px;top:36px;font-size:18px;letter-spacing:-.6px;">Alpine Getaway<small>Journals 2015</small></div>
    <div class="bubble red" style="left:8px;top:95px;width:84px;height:84px;font-size:17px;">What's<br>New</div>
    <div class="bubble navy" style="left:30px;top:146px;width:84px;height:84px;font-size:17px;padding-top:10px;">in<br>2015</div>
    <div class="line-tag bar-left" style="left:3px;top:371px;">The ultimate</div>
    <div class="line-tag bar-left" style="left:3px;top:401px;">guide to</div>
    <div class="line-tag bar-left strong" style="left:3px;top:431px;">holidays in</div>
    <div class="line-tag bar-left strong" style="left:3px;top:461px;">France</div>
    <a class="cta" href="#" style="left:2px;top:556px;width:117px;height:31px;font-size:13px;">More information</a>
  </section>

  <!-- 300 x 250 MPU, town square -->
  <section class="banner mpu" style="left:296px;top:278px;width:303px;height:253px;">
    <div class="photo" role="img" aria-label="Photo of ornate townhouses around a busy square" style="inset:0;background:linear-gradient(180deg,#d8d5d6 0%,#c69a8a 45%,#a98672 75%,#cdbfb5 100%);"></div>
    <div class="fade" style="height:86px;"></div>
    <div class="flag-band"></div>
    <div class="brand" style="left:14px;top:20px;font-size:44px;">Alpine Getaway<small style="color:var(--navy);">Journals 2015</small></div>
    <div class="tag red" style="left:48px;top:109px;height:32px;font-size:17px;">The ultimate guide to</div>
    <div class="tag navy" style="left:41px;top:144px;height:35px;font-size:21px;">holidays in France</div>
    <a class="cta" href="#" style="left:67px;top:203px;width:161px;height:42px;">More information</a>
    <div class="base-band"></div>
  </section>

  <!-- 300 x 250 MPU, château -->
  <section class="banner mpu" style="left:628px;top:278px;width:303px;height:253px;">
    <div class="photo" role="img" aria-label="Photo of a white château over a river with trees" style="inset:0;background:linear-gradient(180deg,#e4ebf2 0%,#c4d2dd 45%,#9fa89c 70%,#6f7a73 100%);"></div>
    <div class="fade" style="height:86px;"></div>
    <div class="brand" style="left:14px;top:18px;font-size:44px;">Alpine Getaway<small style="color:var(--navy);">Journals 2015</small></div>
    <div class="tag red" style="left:56px;top:108px;height:32px;font-size:17px;">The ultimate guide to</div>
    <div class="tag navy" style="left:42px;top:145px;height:35px;font-size:21px;">holidays in France</div>
    <a class="cta" href="#" style="left:67px;top:202px;width:161px;height:42px;">More information</a>
    <div class="base-band"></div>
  </section>

  <!-- 728 x 90 leaderboard, photo -->
  <section class="banner leaderboard" style="left:296px;top:557px;width:735px;height:91px;">
    <div class="photo" role="img" aria-label="Photo of a stone village street under blue sky" style="inset:0;background:linear-gradient(90deg,#6b4a2e 0%,#7d5a3a 35%,#a59a8c 55%,#b8cde0 75%,#7e6a55 100%);"></div>
    <div class="brand on-dark" style="left:16px;top:24px;font-size:33px;">Alpine Getaway<small>Journals 2015</small></div>
    <div class="tag red" style="left:290px;top:12px;height:32px;font-size:17px;">The ultimate guide to</div>
    <div class="tag navy" style="left:276px;top:47px;height:35px;font-size:21px;">holidays in France</div>
    <div style="position:absolute;left:556px;top:15px;color:var(--white);font-weight:700;font-size:16px;text-shadow:0 1px 2px rgba(0,0,0,.5);">What's New in 2015?</div>
    <a class="cta" href="#" style="left:556px;top:44px;width:153px;height:37px;">More information</a>
  </section>

  <!-- 728 x 90 leaderboard, light -->
  <section class="banner leaderboard" style="left:296px;top:679px;width:735px;height:91px;">
    <div class="photo" role="img" aria-label="Faded photo of a château façade" style="left:270px;top:0;width:465px;height:91px;background:linear-gradient(90deg,rgba(238,242,247,1) 0%,#dfe4ea 40%,#d6dbe2 100%);"></div>
    <div class="brand" style="left:27px;top:16px;font-size:46px;">Alpine Getaway<small style="color:var(--navy);">Journals 2015</small></div>
    <div class="line-tag bar-right" style="right:219px;top:9px;">The ultimate</div>
    <div class="line-tag bar-right" style="right:219px;top:34px;">guide to</div>
    <div class="line-tag bar-right strong" style="right:219px;top:58px;">holidays in France</div>
    <div class="bubble red" style="left:560px;top:-26px;width:80px;height:80px;font-size:16px;padding-top:22px;">What's<br>New</div>
    <div class="bubble navy" style="left:612px;top:-34px;width:82px;height:82px;font-size:16px;padding-top:30px;">in<br>2015</div>
    <a class="cta" href="#" style="left:556px;top:44px;width:153px;height:38px;">More information</a>
  </section>

</body>
</html>
```